Electrical needs letterhead design

Need a letterhead design for an electrical company. Using the same colours as to what are used in the logo.
After a modern design.

Want the logo in top right or top left.

Must include...

ABN 71 804 239 356
PHONE 0458203917
www.kelmaroo.com.au
jed@kelmaroo.com.au

'ABN' and 'PHONE' in bold.

Keep it basic. Logo top left, details either next to it or far right corner. Dont want any other objects included.

Electrical

```html
<!DOCTYPE html>
<html lang="en">
<head>
<meta charset="utf-8">
<title>Kelmaroo Electrical Solutions – Letterhead</title>
<link href="https://fonts.googleapis.com/css2?family=Open+Sans:wght@400;600;700&display=swap" rel="stylesheet">
<style>
  :root {
    --backdrop: #8f8f8f;
    --paper: #ffffff;
    --brand-red: #8b1e1c;
    --brand-deep: #7d1f1d;
    --brand-orange: #d9412a;
    --ink: #2b2b2b;
    --muted: #8a8a8a;
    --watermark: #ededed;
  }
  * { margin: 0; padding: 0; box-sizing: border-box; }
  html, body {
    width: 1200px; height: 640px; overflow: hidden;
    background: var(--backdrop);
    font-family: "Open Sans", Arial, sans-serif;
  }
  .letterhead {
    position: absolute; left: 387px; top: 20px;
    width: 426px; height: 600px;
    background: var(--paper);
    box-shadow: 0 1px 3px rgba(0,0,0,.25);
    overflow: hidden;
  }
  .top-rule {
    position: absolute; left: 0; top: 0; width: 100%; height: 4px;
    background: var(--brand-red);
  }
  .brand { position: absolute; left: 37px; top: 34px; }
  .brand-name {
    display: flex; align-items: center; gap: 5px;
    font-size: 27px; font-weight: 600; color: var(--brand-red);
    line-height: 1; letter-spacing: -0.3px;
  }
  .brand-dot {
    width: 9px; height: 9px; border-radius: 50%;
    background: var(--brand-red);
  }
  .brand-tagline {
    margin-top: 3px; margin-left: 2px;
    font-size: 5px; letter-spacing: 2.6px; color: var(--muted);
    text-transform: uppercase;
  }
  .sender {
    position: absolute; right: 108px; top: 41px; text-align: right;
  }
  .sender-name { font-size: 8px; font-weight: 700; color: var(--brand-red); line-height: 1.2; }
  .sender-abn { font-size: 5.5px; color: var(--ink); }
  .sender-abn b { font-weight: 700; }
  .divider {
    position: absolute; left: 323px; top: 36px; width: 1px; height: 27px;
    background: #c9c9c9;
  }
  .contacts {
    position: absolute; left: 329px; top: 36px; list-style: none;
    font-size: 5.5px; color: var(--ink);
  }
  .contacts li { display: flex; align-items: center; gap: 3px; height: 9px; }
  .contacts b { font-weight: 700; }
  .contact-icon {
    width: 6px; height: 6px; border-radius: 50%;
    background: var(--brand-red); display: inline-flex;
    align-items: center; justify-content: center;
  }
  .watermark {
    position: absolute; left: 125px; top: 224px;
    width: 176px; height: 176px; border-radius: 50%;
    background: var(--watermark);
  }
  .footer-bands { position: absolute; left: 0; bottom: 0; }
</style>
</head>
<body>
  <main class="letterhead">
    <div class="top-rule"></div>

    <header class="brand">
      <div class="brand-name"><span class="brand-dot"></span>Kelmaroo</div>
      <div class="brand-tagline">Electrical Solutions</div>
    </header>

    <div class="sender">
      <div class="sender-name">Jed Harlow</div>
      <div class="sender-abn"><b>ABN</b> 71 804 239 356</div>
    </div>
    <div class="divider"></div>
    <ul class="contacts">
      <li>
        <span class="contact-icon">
          <svg width="4" height="4" viewBox="0 0 10 10"><path d="M2 1l2 2-1 1.5c.8 1.4 1.6 2.2 3 3L7.5 6.5l2 2L8 10C4 9.5.5 6 0 2z" fill="#fff"/></svg>
        </span>
        <span><b>PHONE</b> 0458203917</span>
      </li>
      <li>
        <span class="contact-icon">
          <svg width="4" height="4" viewBox="0 0 10 10"><rect x="0.5" y="2" width="9" height="6" fill="none" stroke="#fff" stroke-width="1.3"/><path d="M.5 2l4.5 3.5L9.5 2" fill="none" stroke="#fff" stroke-width="1.3"/></svg>
        </span>
        <span>jed@kelmaroo.com.au</span>
      </li>
      <li>
        <span class="contact-icon">
          <svg width="4" height="4" viewBox="0 0 10 10"><circle cx="5" cy="5" r="4" fill="none" stroke="#fff" stroke-width="1.2"/><path d="M1 5h8M5 1c-2 2.5-2 5.5 0 8M5 1c2 2.5 2 5.5 0 8" fill="none" stroke="#fff" stroke-width="1"/></svg>
        </span>
        <span>www.kelmaroo.com.au</span>
      </li>
    </ul>

    <div class="watermark" aria-hidden="true"></div>

    <svg class="footer-bands" width="426" height="22" viewBox="0 0 426 22" aria-hidden="true">
      <polygon points="0,9 251,9 247,22 0,22" fill="var(--brand-orange)"/>
      <path d="M262,22 L266,6 Q267,1 273,1 L426,1 L426,22 Z" fill="var(--brand-deep)"/>
    </svg>
  </main>
</body>
</html>
```